Simple Business Cards for Self-employed Coach

Simple business card with a design that includes the QLT logo.
Using either only the logo color or additional colors that match the logo.

Meridian Guides reach deeply into the past, gathering wisdom from East and West, while still staying current with the frontiers of new discovery in cognitive science, genetics, and other disciplines. see https://www.brightharborpath.example/what-is-integral-coaching/

Target Market(s)

Coaching Clients in Tokyo /Asia; in business organizations, but also outside

Industry/Entity Type

Life Coaching

Contact Information for Business Card

Lukas Brenning
Certified Meridian Guide

3-2-48 Kamiyoshi
Nakarino 164-0392
Tokyo, Japan

Phone: +81 70 4817 5062
E-Mail: lukas.brenning@mailora.example

Font styles to use
Sans Serif

Colors
00a990

Requirements
Must have
• include uploaded logo
• color fitting with QLT logo color
Nice to have
• simple, elegant design
Should not have
• clutter

```html
<!DOCTYPE html>
<html lang="en">
<head>
<meta charset="utf-8">
<title>QLT – Business Card</title>
<link href="https://fonts.googleapis.com/css2?family=Arimo:wght@400;700&family=Roboto:wght@300;400&display=swap" rel="stylesheet">
<style>
  :root {
    --teal: #0f8478;
    --teal-brand: #00a990;
    --ink: #6d6e70;
    --ink-soft: #8a8b8d;
    --card: #ffffff;
    --backdrop: #e9ebea;
  }
  * { box-sizing: border-box; margin: 0; padding: 0; }
  html, body {
    width: 1200px;
    height: 950px;
    overflow: hidden;
    background: var(--backdrop);
  }
  .stage {
    width: 1200px;
    height: 950px;
    display: flex;
    align-items: center;
    justify-content: center;
  }
  .card {
    position: relative;
    width: 1000px;
    height: 570px;
    background: var(--card);
    box-shadow: 0 2px 10px rgba(0,0,0,0.08);
    font-family: "Roboto", Arial, sans-serif;
    color: var(--ink);
  }
  .brand {
    position: absolute;
    left: 90px;
    top: 100px;
    display: flex;
    align-items: center;
    gap: 18px;
  }
  .brand-square {
    width: 64px;
    height: 64px;
    background: var(--teal);
  }
  .brand-name {
    font-family: "Arimo", Arial, sans-serif;
    font-weight: 700;
    font-size: 66px;
    letter-spacing: 14px;
    color: var(--teal);
    line-height: 1;
  }
  .person {
    position: absolute;
    left: 340px;
    top: 262px;
  }
  .person-name {
    font-family: "Arimo", Arial, sans-serif;
    font-weight: 700;
    font-size: 30px;
    color: var(--teal);
  }
  .person-title {
    margin-top: 6px;
    font-size: 21px;
    font-weight: 400;
    color: var(--ink);
  }
  .rule {
    position: absolute;
    height: 1px;
    background: var(--teal);
  }
  .rule-address { right: 60px; width: 260px; top: 90px; }
  .rule-contact { left: 60px; width: 260px; top: 390px; }
  .address {
    position: absolute;
    right: 60px;
    top: 110px;
    text-align: right;
    font-size: 19px;
    font-weight: 300;
    line-height: 1.45;
    color: var(--ink);
  }
  .contact {
    position: absolute;
    left: 60px;
    top: 408px;
    font-size: 19px;
    font-weight: 300;
    line-height: 1.45;
    color: var(--ink);
  }
  .contact-label {
    font-weight: 400;
    color: var(--teal);
  }
</style>
</head>
<body>
  <main class="stage">
    <article class="card">
      <div class="brand">
        <span class="brand-square" aria-hidden="true"></span>
        <span class="brand-name">QLT</span>
      </div>

      <div class="person">
        <p class="person-name">Lukas Brenning</p>
        <p class="person-title">Certified Meridian Guide</p>
      </div>

      <span class="rule rule-address"></span>
      <address class="address">
        3-2-48 Kamiyoshi<br>
        Nakarino 164-0392<br>
        Tokyo, Japan
      </address>

      <span class="rule rule-contact"></span>
      <div class="contact">
        <p><span class="contact-label">P</span> : +81 70 4817 5062</p>
        <p>lukas.brenning@mailora.example</p>
        <p>www.brightharborpath.example</p>
      </div>
    </article>
  </main>
</body>
</html>
```